Design professional label for greener chemicals (cleaning and lubrication) brand

Design a b2b professional label that is based on the examples given.
Size: 135 x 200 mm, please use text of the label description doc (only the kalmir stainless steel polish example design document has the right text and size)
It should include:
1. Logo, can be fully changed except the shape of "KALMIR", colors and fonts of the rest can be customized
2. Focus should be on professional market, we would like to express the professionalism and high quality of the product
3. Focus should be on our brand name "KALMIR CLEANER COMPOUNDS"
4. Should include product name, product description, danger sentences, danger symbol, user instructions, image
5. Should include numbers that explain what the product does: 1. Prewash 2. Clean 3. Protect 4. Preserve and highlight number 2.

Target Market(s)

Professional cleaning companies, steel industry, food industry, pharmacy industry

Industry/Entity Type

Cleaning industry, steel industry, food industry, boat cleaning, car cleaning, professional lubrication

Font styles to use
Sans Serif

Requirements
Must have
• Professional look, clean look, image, focus on our brand name
Nice to have
• Numbers (see explanation), label divided in three parts (logo and product name and image in the middle as the highlight)

```html
<!DOCTYPE html>
<html lang="en">
<head>
<meta charset="utf-8">
<title>Kalmir Stainless Steel Polish Label</title>
<link rel="stylesheet" href="https://fonts.googleapis.com/css2?family=Alfa+Slab+One&family=Roboto+Condensed:wght@500;700&display=swap">
<style>
  :root {
    --stage: #000000;
    --navy: #0f1a2c;
    --chevron: #1d3461;
    --chevron-edge: #2a3550;
    --teal: #14889b;
    --teal-light: #2a9fb0;
    --band-blue: #233f78;
    --white: #ffffff;
    --muted: #c3cbd6;
    --danger: #d8202a;
  }
  * { margin: 0; padding: 0; box-sizing: border-box; }
  html, body { width: 1200px; height: 1200px; overflow: hidden; background: var(--stage); }
  .stage { width: 1200px; height: 1200px; display: flex; align-items: center; justify-content: center; }
  .label { position: relative; width: 675px; height: 1000px; background: var(--navy); overflow: hidden; }
  .label-art { position: absolute; inset: 0; }

  .use-ribbon {
    position: absolute; left: 40px; top: 150px; width: 82px; height: 460px;
    display: flex; flex-direction: column; align-items: center; gap: 26px; padding-top: 30px;
    font-family: "Roboto Condensed", sans-serif; color: var(--white); text-align: center;
  }
  .use-item { display: flex; flex-direction: column; align-items: center; gap: 6px; font-size: 10px; font-weight: 500; line-height: 1.05; }
  .use-item svg { width: 40px; height: 34px; }

  .title-block { position: absolute; left: 60px; right: 40px; top: 575px; font-family: "Alfa Slab One", serif; text-align: right; }
  .kicker { color: var(--teal); font-size: 40px; letter-spacing: 1px; line-height: 1; }
  .product-name { color: var(--white); font-size: 118px; line-height: 1; margin-top: 6px; letter-spacing: 1px; font-weight: 400; }
  .claim { display: inline-block; background: var(--band-blue); color: var(--white); font-size: 31px; padding: 4px 10px; margin-top: 6px; line-height: 1; }
  .feature { color: var(--white); font-size: 50px; line-height: 1; margin-top: 6px; }

  .web-band {
    position: absolute; left: 0; right: 0; top: 860px; height: 42px; background: var(--teal);
    font-family: "Alfa Slab One", serif; color: var(--white); font-size: 22px;
    display: flex; align-items: center; justify-content: flex-end; padding-right: 40px;
  }
  .eco-mark { position: absolute; left: 46px; top: 888px; width: 70px; height: 70px; border-radius: 50%; background: var(--teal-light); border: 3px solid var(--navy); }

  .brand-strip { position: absolute; left: 130px; top: 908px; width: 430px; color: var(--white); font-family: "Roboto Condensed", sans-serif; }
  .brand-name { font-family: "Alfa Slab One", serif; font-size: 21px; line-height: 1; letter-spacing: 0.5px; font-weight: 400; }
  .steps { display: flex; gap: 14px; margin-top: 7px; list-style: none; font-size: 12px; font-weight: 700; }
  .step { display: flex; align-items: center; gap: 4px; color: var(--muted); }
  .step-num { width: 16px; height: 16px; border-radius: 50%; border: 1.5px solid var(--muted); display: flex; align-items: center; justify-content: center; font-size: 10px; }
  .step.is-key { background: var(--teal); color: var(--white); padding: 1px 6px 1px 2px; }
  .step.is-key .step-num { border-color: var(--white); background: var(--white); color: var(--teal); }
  .fine-print { margin-top: 6px; font-size: 9.5px; font-weight: 500; line-height: 1.25; color: var(--muted); }
  .fine-print b { color: var(--white); }

  .hazard { position: absolute; right: 40px; top: 916px; width: 62px; height: 62px; }
</style>
</head>
<body>
<main class="stage">
  <section class="label">
    <svg class="label-art" viewBox="0 0 675 1000" width="675" height="1000">
      <defs>
        <linearGradient id="photoTone" x1="0" y1="0" x2="1" y2="1">
          <stop offset="0" stop-color="#d6dade"/>
          <stop offset="0.45" stop-color="#9aa2aa"/>
          <stop offset="0.7" stop-color="#7fb892"/>
          <stop offset="1" stop-color="#6b7279"/>
        </linearGradient>
      </defs>
      <polygon class="photo-area" role="img" aria-label="Photo of a gloved hand wiping a stainless steel surface with a green cloth" points="0,0 675,0 675,170 380,470 0,90" fill="url(#photoTone)"/>
      <polyline class="chevron" points="-20,70 380,470 700,150" fill="none" stroke="var(--chevron)" stroke-width="46"/>
      <polyline class="chevron-edge" points="-20,130 380,530 700,210" fill="none" stroke="var(--chevron-edge)" stroke-width="6"/>
      <polygon class="ribbon" points="40,150 122,150 122,610 81,580 40,610" fill="var(--teal)"/>
    </svg>

    <div class="use-ribbon">
      <div class="use-item">
        <svg viewBox="0 0 40 34"><path d="M4 20 L36 20 L30 28 L9 28 Z" fill="#fff"/><path d="M12 20 L16 12 L28 12 L30 20 Z" fill="#fff"/></svg>
        <span>BOATS</span>
      </div>
      <div class="use-item">
        <svg viewBox="0 0 40 34"><circle cx="20" cy="17" r="11" fill="none" stroke="#fff" stroke-width="5" stroke-dasharray="4 3"/><circle cx="20" cy="17" r="5" fill="#fff"/></svg>
        <span>INDUSTRIAL STEEL SURFACES</span>
      </div>
      <div class="use-item">
        <svg viewBox="0 0 40 34"><path d="M14 2 L26 2 L26 8 L34 14 L6 14 L14 8 Z" fill="#fff"/><rect x="10" y="19" width="20" height="13" fill="none" stroke="#fff" stroke-width="3"/><line x1="10" y1="25" x2="30" y2="25" stroke="#fff" stroke-width="2"/></svg>
        <span>STAINLESS STEEL KITCHENS</span>
      </div>
    </div>

    <div class="title-block">
      <p class="kicker">STAINLESS STEEL</p>
      <h1 class="product-name">POLISH</h1>
      <p class="claim">RESTORE STEEL SURFACES</p>
      <p class="feature">HOLOGRAM FREE</p>
    </div>

    <div class="web-band">www.kalmirchemicals.com</div>
    <div class="eco-mark" aria-hidden="true"></div>

    <div class="brand-strip">
      <p class="brand-name">KALMIR CLEANER COMPOUNDS</p>
      <ol class="steps">
        <li class="step"><span class="step-num">1</span>PREWASH</li>
        <li class="step is-key"><span class="step-num">2</span>CLEAN</li>
        <li class="step"><span class="step-num">3</span>PROTECT</li>
        <li class="step"><span class="step-num">4</span>PRESERVE</li>
      </ol>
      <p class="fine-print"><b>Use:</b> Apply to a dry cloth, wipe along the grain, buff with clean microfibre.<br>
      <b>Warning:</b> Causes serious eye irritation. Keep out of reach of children.</p>
    </div>

    <svg class="hazard" viewBox="0 0 62 62" role="img" aria-label="Hazard pictogram: exclamation mark">
      <rect x="12" y="12" width="38" height="38" transform="rotate(45 31 31)" fill="#fff" stroke="var(--danger)" stroke-width="4"/>
      <rect x="28.5" y="17" width="5" height="20" rx="1.5" fill="#000"/>
      <circle cx="31" cy="43" r="3" fill="#000"/>
    </svg>
  </section>
</main>
</body>
</html>
```